The Amp Fellow

need a business card for a dj and sound equipment hire(rentals) business based in Melbourne. i have attached a current card get an idea. card needs to be unique professional looking.

ps.this card is not for a DJ. it's a rental business of dj equipment and pa systems.

Industry/Entity Type

Business

Font styles to use
Sans Serif
Script

Requirements
Must have
• Business Name: THE AMP FELLOW
Contact Person: RAVINDU PERERALA
Mobile: 047 BASSY 82
Email: RAVINDU@THEAMPFELLOW.COM.AU
Website: WWW.THEAMPFELLOW.COM.AU
Facebook: WWW.FACEBOOK.CM/THEAMPFELLOW.COM.AU

```html
<!DOCTYPE html>
<html lang="en">
<head>
<meta charset="utf-8">
<title>The Amp Fellow — Business Card</title>
<link rel="stylesheet" href="https://fonts.googleapis.com/css2?family=Josefin+Sans:wght@300;400&display=swap">
<style>
  :root {
    --page: #ffffff;
    --card: #000000;
    --ring: #3a3a3a;
    --ring-soft: #222222;
    --text: #ffffff;
    --accent: #4fd6c4;
    --icon: #2f9be0;
    --rule: #9a9a9a;
  }
  * { margin: 0; padding: 0; box-sizing: border-box; }
  html, body {
    width: 1200px; height: 900px; overflow: hidden;
    background: var(--page);
    font-family: "Josefin Sans", sans-serif;
    color: var(--text);
  }
  .canvas { position: relative; width: 1200px; height: 900px; }
  .card {
    position: absolute; width: 710px; height: 405px;
    background: var(--card); overflow: hidden;
    box-shadow: 2px 3px 4px rgba(0,0,0,0.25);
  }
  .card--front { left: 88px; top: 15px; }
  .card--back { left: 400px; top: 470px; }
  .card__rings { position: absolute; inset: 0; }

  .contact-person {
    position: absolute; left: 36px; top: 205px;
    transform: rotate(-20deg); transform-origin: left top;
    width: 240px;
  }
  .contact-person__name {
    font-weight: 300; font-size: 20px; letter-spacing: 1.2px;
    color: var(--accent); white-space: nowrap;
    padding-bottom: 3px; border-bottom: 1.5px solid var(--accent);
  }
  .contact-person__phone {
    font-weight: 300; font-size: 12px; letter-spacing: 1.6px;
    text-align: right; margin-top: 6px; white-space: nowrap;
  }

  .contact-list {
    position: absolute; left: 430px; top: 16px;
    padding: 6px 0 6px 14px; border-left: 1.5px solid var(--rule);
    list-style: none;
  }
  .contact-list__item {
    display: flex; align-items: center; gap: 10px;
    font-weight: 300; font-size: 11px; letter-spacing: 0.8px;
    height: 21px; white-space: nowrap;
  }
  .contact-list__icon { width: 13px; height: 13px; flex: none; }

  .brand-name {
    position: absolute; font-weight: 300; color: var(--text);
    white-space: nowrap; letter-spacing: 1px;
  }
  .card--front .brand-name { right: 28px; bottom: 50px; font-size: 38px; }
  .card--back .brand-name { right: 40px; bottom: 112px; font-size: 54px; }
</style>
</head>
<body>
<main class="canvas">

  <section class="card card--front" aria-label="Card front with contact details">
    <svg class="card__rings" width="710" height="405" aria-hidden="true">
      <circle cx="165" cy="225" r="172" fill="none" stroke="var(--ring-soft)" stroke-width="3"/>
      <circle cx="165" cy="225" r="158" fill="none" stroke="var(--ring)" stroke-width="12"/>
    </svg>

    <div class="contact-person">
      <p class="contact-person__name">RAVINDU PERERALA</p>
      <p class="contact-person__phone">047 BASSY 82</p>
    </div>

    <ul class="contact-list">
      <li class="contact-list__item">
        <svg class="contact-list__icon" viewBox="0 0 14 14" aria-hidden="true">
          <circle cx="7" cy="7" r="7" fill="var(--icon)"/>
          <rect x="3.5" y="4.5" width="7" height="5" fill="none" stroke="#fff" stroke-width="1"/>
          <path d="M3.5 4.5 L7 7.5 L10.5 4.5" fill="none" stroke="#fff" stroke-width="1"/>
        </svg>
        RAVINDU@THEAMPFELLOW.COM.AU
      </li>
      <li class="contact-list__item">
        <svg class="contact-list__icon" viewBox="0 0 14 14" aria-hidden="true">
          <circle cx="7" cy="7" r="7" fill="var(--icon)"/>
          <path d="M3.5 7 L7 4 L10.5 7 M4.5 6.5 V10 H9.5 V6.5" fill="none" stroke="#fff" stroke-width="1"/>
        </svg>
        WWW.THEAMPFELLOW.COM.AU
      </li>
      <li class="contact-list__item">
        <svg class="contact-list__icon" viewBox="0 0 14 14" aria-hidden="true">
          <circle cx="7" cy="7" r="7" fill="var(--icon)"/>
        </svg>
        /THEAMPFELLOW.COM.AU
      </li>
    </ul>

    <p class="brand-name">THE AMP FELLOW</p>
  </section>

  <section class="card card--back" aria-label="Card back with business name">
    <svg class="card__rings" width="710" height="405" aria-hidden="true">
      <circle cx="52" cy="125" r="118" fill="none" stroke="var(--ring-soft)" stroke-width="10"/>
      <circle cx="52" cy="125" r="100" fill="none" stroke="var(--ring-soft)" stroke-width="2"/>
      <circle cx="130" cy="320" r="118" fill="none" stroke="var(--ring-soft)" stroke-width="10"/>
      <circle cx="130" cy="320" r="100" fill="none" stroke="var(--ring-soft)" stroke-width="2"/>
    </svg>

    <p class="brand-name">THE AMP FELLOW</p>
  </section>

</main>
</body>
</html>
```